large sticker 80 cms high for 139 cm wide for medical laser center window

For a medical laser center. Tou will have to use my logo. I don't know at this time if i want just the logo and a list of what i propose, or just logo and pictures that evoke the different traitements:
"Réjuvénation vaginale Laser
Laser vasculaire
Taches pigmentaires Laser
Epilation Laser"

Colors

Designer to choose colors to be used in the design.

```html
<!DOCTYPE html>
<html lang="fr">
<head>
<meta charset="utf-8">
<title>Clinique Lumen – vitrophanie</title>
<link rel="stylesheet" href="https://fonts.googleapis.com/css2?family=Lato:wght@300;400&display=swap">
<style>
  :root {
    --backdrop: #d4d5d7;
    --ink-dark: #0b0b0c;
    --slate: #5b5a60;
    --slate-light: #67666c;
    --gold-deep: #b07a4a;
    --gold-text: #c4935c;
    --gold-light: #e9c97f;
    --white: #ffffff;
    --brand-grey: #5c5c5e;
  }
  * { margin: 0; padding: 0; box-sizing: border-box; }
  html, body {
    width: 1200px; height: 734px; overflow: hidden;
    background: var(--backdrop);
    font-family: "Lato", sans-serif;
  }
  .banner {
    position: absolute; left: 173.5px; top: 109.7px;
    width: 878px; height: 506px; overflow: hidden;
  }
  .banner-shapes { position: absolute; inset: 0; width: 100%; height: 100%; display: block; }
  .treatments { position: absolute; left: 0; top: 0; list-style: none; }
  .treatment {
    position: absolute; left: 36px; white-space: nowrap;
    display: flex; align-items: center; gap: 7px;
    color: var(--white); font-size: 25px; font-weight: 300; line-height: 1;
  }
  .treatment-icon { width: 17px; height: 17px; flex: none; }
  .booking {
    position: absolute; left: 34px; top: 452px;
    color: var(--gold-text); font-size: 16.5px; font-weight: 300; line-height: 1; white-space: nowrap;
  }
  .contact {
    position: absolute; left: 34px; top: 472px;
    color: var(--white); font-size: 16px; font-weight: 300; line-height: 1; white-space: nowrap;
  }
  .brand {
    position: absolute; left: 560px; top: 444px; width: 250px;
    text-align: center;
  }
  .brand-name { color: var(--brand-grey); font-size: 38px; font-weight: 300; line-height: 1; white-space: nowrap; }
</style>
</head>
<body>
  <section class="banner">
    <svg class="banner-shapes" viewBox="0 0 1801 1038" preserveAspectRatio="none">
      <defs>
        <linearGradient id="sky" x1="0" y1="0" x2="1" y2="1">
          <stop offset="0" stop-color="#9a9ea3"/>
          <stop offset="0.4" stop-color="#d2d4d6"/>
          <stop offset="0.75" stop-color="#a9abad"/>
          <stop offset="1" stop-color="#8e8f91"/>
        </linearGradient>
        <linearGradient id="gold" x1="0" y1="0" x2="1" y2="0">
          <stop offset="0" stop-color="#b07a4a"/>
          <stop offset="0.25" stop-color="#e9c97f"/>
          <stop offset="0.7" stop-color="#dcb37a"/>
          <stop offset="1" stop-color="#a86a34"/>
        </linearGradient>
        <linearGradient id="goldEdge" x1="0" y1="1" x2="1" y2="0">
          <stop offset="0" stop-color="#a86a34"/>
          <stop offset="0.4" stop-color="#d9b07a"/>
          <stop offset="1" stop-color="#a86a34"/>
        </linearGradient>
        <linearGradient id="slate" x1="0" y1="0" x2="1" y2="0">
          <stop offset="0" stop-color="#0b0b0c"/>
          <stop offset="0.09" stop-color="#47464a"/>
          <stop offset="0.4" stop-color="#5b5a60"/>
          <stop offset="1" stop-color="#67666c"/>
        </linearGradient>
      </defs>

      <rect class="photo-area" x="0" y="0" width="1801" height="720" fill="url(#sky)"
        role="img" aria-label="Photo en noir et blanc : pile de galets gris en équilibre devant un ciel nuageux"/>

      <path class="gold-band" fill="url(#gold)"
        d="M0,458 C200,440 400,440 600,470 C900,520 1100,640 1350,655 C1550,660 1720,610 1801,565
           L1801,595 C1720,640 1550,680 1350,672 C1100,660 900,545 600,510 C350,480 150,500 0,560 Z"/>
      <path class="white-rule" fill="none" stroke="#ffffff" stroke-width="9"
        d="M0,552 C150,492 350,472 600,502 C900,537 1100,652 1350,664 C1550,672 1720,632 1801,588"/>
      <path class="slate-field" fill="url(#slate)"
        d="M0,560 C150,500 350,480 600,510 C900,545 1100,660 1350,672 C1550,680 1720,640 1801,595 L1801,1038 L0,1038 Z"/>
      <path class="brand-panel" fill="#ffffff"
        d="M834,1038 C834,880 905,760 1100,750 C1400,740 1650,725 1801,605 L1801,1038 Z"/>
      <path class="brand-panel-edge" fill="none" stroke="url(#goldEdge)" stroke-width="10"
        d="M834,1038 C834,880 905,760 1100,750 C1400,740 1650,725 1801,605"/>
    </svg>

    <ul class="treatments">
      <li class="treatment" style="top:287px">
        <svg class="treatment-icon" viewBox="0 0 20 20"><circle cx="10" cy="10" r="8.5" fill="none" stroke="#c89a5e" stroke-width="2"/><path d="M8.3,6 L12.3,10 L8.3,14" fill="none" stroke="#c89a5e" stroke-width="2.2"/></svg>
        Réjuvénation vaginale Laser
      </li>
      <li class="treatment" style="top:328px">
        <svg class="treatment-icon" viewBox="0 0 20 20"><circle cx="10" cy="10" r="8.5" fill="none" stroke="#c89a5e" stroke-width="2"/><path d="M8.3,6 L12.3,10 L8.3,14" fill="none" stroke="#c89a5e" stroke-width="2.2"/></svg>
        Laser vasculaire
      </li>
      <li class="treatment" style="top:369px">
        <svg class="treatment-icon" viewBox="0 0 20 20"><circle cx="10" cy="10" r="8.5" fill="none" stroke="#c89a5e" stroke-width="2"/><path d="M8.3,6 L12.3,10 L8.3,14" fill="none" stroke="#c89a5e" stroke-width="2.2"/></svg>
        Laser pour tâches pigmentaires
      </li>
      <li class="treatment" style="top:410px">
        <svg class="treatment-icon" viewBox="0 0 20 20"><circle cx="10" cy="10" r="8.5" fill="none" stroke="#c89a5e" stroke-width="2"/><path d="M8.3,6 L12.3,10 L8.3,14" fill="none" stroke="#c89a5e" stroke-width="2.2"/></svg>
        Epilation Laser
      </li>
    </ul>

    <p class="booking">rdv en ligne sur MediRdv</p>
    <p class="contact">05 61 48 27 90 | cliniquelumen-laser.fr</p>

    <div class="brand">
      <span class="brand-name">Clinique Lumen</span>
    </div>
  </section>
</body>
</html>
```